Web Design Services Create a Similar website to my Competitor

We would like a similar website designed like our main competitor with all the features there website has and more. Also we would like to accept payments through our website and to rank quickly with seo based on our home page and other page use of high traffic keywords. this is the website we would like to have ours designed similar to https://www.festivalpaintbay.com. we will be providing the same services and more just at a different location. We would also like to know be able to easily make adjustments to the website when its time to edit it please thanks.

Basically I am looking to have have similar website built almost exactly the same but with my logo, and other personalized information to my company Orla Maskrade Beauty Lounge. I will need to send you model images and logo design idea but the body and user interface of my competitor https://www.festivalpaintbay.com will be exactly the same. I can be reached anytime to answer any questions you may have.
Updates

Hi Designers I would like to clarify some information Festival Paint Bay is my Competitor we are not affiliated. I would like my website to be designed similar to hers but please do not take any content from her website to put on mine I will be providing images to be posted on my website. Also please do not use any of her videos or ClipTube videos on my website to avoid any legal issues. Thanks for your understanding.

Target Market(s)

Make up Application Services For Events and Trinidad and Tobago Carnival

Industry/Entity Type

Beauty and Makeup Application and services

Coding

Coded - Design and coding required

Number of Pages Required

5+ page

Font styles to use
Sans Serif

Colors
E54698
E96AAD
F1A4CE
F9D9EA
FCEFF6
A7469A
B969AE
D3A5CF
EDDBEB
F8F0F9

Requirements
Must have
• Must be similar to my competitor, need a video section, testimonial and must be easily able to navigate to information sections and book now payment notifications running on all pages so customers can easily book there spot for 2026 carnival
Nice to have
• I am looking to have a similar website to https://www.festivalpaintbay.com created but make it as minimal and modern
Should not have
• Project can be coded if it makes it easier to create a similar look to my competitor just ask that updates can easily be made later on.

```html
<!DOCTYPE html>
<html lang="en">
<head>
<meta charset="utf-8">
<title>Orla Maskrade Beauty Lounge – Home Page Layouts</title>
<link rel="stylesheet" href="https://fonts.googleapis.com/css2?family=Fraunces:opsz,wght@9..144,600&family=Nunito:wght@400;500&display=swap">
<style>
  :root {
    --stage: #c07a73;
    --white: #ffffff;
    --berry: #b02a62;
    --berry-deep: #ab2760;
    --nav: #b8306f;
    --blush: #ffcac4;
    --cream: #fbe8e4;
    --lilac: #d8b1df;
    --hero-text: #ffd0c8;
    --button: #f7c4d8;
    --button-text: #9d2c67;
    --service-line: #f3c9da;
    --serif: "Fraunces", Georgia, serif;
    --sans: "Nunito", Arial, sans-serif;
  }
  * { box-sizing: border-box; margin: 0; padding: 0; }
  html, body { width: 1200px; height: 1200px; overflow: hidden; }
  body { background: var(--stage); position: relative; font-family: var(--sans); }

  .page { position: absolute; overflow: hidden; background: var(--cream); box-shadow: 4px 6px 10px rgba(60, 20, 20, .35); }

  /* ---------- secondary page (behind) ---------- */
  .page--scroll { left: 657px; top: 56px; width: 486px; height: 1125px; }
  .page--scroll .site-header { height: 35px; }
  .page--scroll .brand { left: 38px; top: 11px; gap: 4px; }
  .page--scroll .brand-dot { width: 12px; height: 12px; }
  .page--scroll .brand-name { font-size: 7.5px; line-height: 7.5px; }
  .page--scroll .main-nav { right: 38px; top: 19px; gap: 9px; font-size: 7.5px; }
  .page--scroll .hero { top: 35px; height: 270px; }
  .page--scroll .hero-title { left: 37px; top: 137px; font-size: 27.5px; line-height: 30px; }
  .page--scroll .band { top: 305px; height: 17px; }

  .scroll-intro { position: absolute; left: 0; top: 322px; width: 486px; height: 175px; background: var(--blush); }
  .scroll-intro p { position: absolute; right: 39px; top: 43px; width: 260px; text-align: right; font-size: 7.3px; line-height: 9px; color: var(--berry); }
  .scallop--scroll { position: absolute; left: 0; top: 497px; width: 486px; height: 21px; }

  .why-title { position: absolute; left: 110px; top: 521px; width: 290px; text-align: center; font-family: var(--serif); font-weight: 600; font-size: 22px; line-height: 23px; color: var(--berry); }
  .why-text { position: absolute; left: 170px; top: 596px; width: 170px; font-size: 7px; line-height: 9px; color: #4a2a33; }

  .gallery-photo { position: absolute; border-radius: 2px; }
  .gallery-photo--one { left: 170px; top: 665px; width: 65px; height: 141px; background: linear-gradient(160deg, #8a6a55, #c9a27c 55%, #5b4a3a); }
  .gallery-photo--two { left: 250px; top: 631px; width: 92px; height: 141px; background: radial-gradient(circle at 50% 35%, #7a7f85, #2f3338 65%, #1c1e21); }
  .gallery-photo--three { left: 356px; top: 665px; width: 92px; height: 141px; background: radial-gradient(circle at 55% 40%, #f1ece8, #a9b3c8 55%, #3e4a6a); }
  .gallery-arrow { position: absolute; left: 455px; top: 720px; width: 14px; height: 28px; }

  .services { position: absolute; left: 34px; top: 857px; width: 410px; height: 268px; background: var(--berry-deep); }
  .services-photo { position: absolute; left: 26px; top: 107px; width: 138px; height: 133px; border-radius: 12px; background: linear-gradient(180deg, #2a1a22, #3a6a86 45%, #1d1418); outline: 2px solid #ffd6e4; outline-offset: 3px; }
  .services-title { position: absolute; right: 21px; top: 37px; font-family: var(--serif); font-weight: 600; font-size: 20px; color: #fde6ee; }
  .services-sub { position: absolute; right: 21px; top: 65px; width: 190px; text-align: right; font-size: 7px; line-height: 9px; color: #fde6ee; }
  .service-list { position: absolute; right: 19px; top: 106px; list-style: none; display: flex; flex-direction: column; gap: 9px; }
  .service-item { width: 118px; height: 15px; border: 1px solid var(--service-line); border-radius: 8px; display: flex; justify-content: space-between; align-items: center; padding: 0 6px; color: #fde6ee; font-size: 7px; }
  .service-item small { font-size: 3.5px; opacity: .85; }

  /* ---------- main page (front) ---------- */
  .page--home { left: 32px; top: 136px; width: 828px; height: 884px; }
  .site-header { position: absolute; left: 0; top: 0; width: 100%; height: 59px; background: var(--white); }
  .brand { position: absolute; left: 63px; top: 14px; display: flex; align-items: center; gap: 6px; }
  .brand-dot { width: 28px; height: 28px; border-radius: 50%; background: #ecc6dd; }
  .brand-name { font-family: var(--serif); font-weight: 600; font-size: 13px; line-height: 13px; color: #a9468f; }
  .main-nav { position: absolute; right: 63px; top: 33px; display: flex; gap: 15px; list-style: none; font-size: 12.5px; color: var(--nav); }

  .hero { position: absolute; left: 0; top: 59px; width: 100%; height: 462px; background:
      radial-gradient(ellipse 30% 35% at 68% 30%, #d9c79a 0%, rgba(217,199,154,0) 100%),
      radial-gradient(ellipse 25% 40% at 66% 65%, #caa08a 0%, rgba(202,160,138,0) 100%),
      linear-gradient(120deg, #0f2a1c, #1e4a30 45%, #14301f); }
  .hero-title { position: absolute; left: 63px; top: 368px; font-family: var(--serif); font-weight: 600; font-size: 47px; line-height: 51px; color: var(--hero-text); }
  .book-button { position: absolute; left: 65px; top: 471px; width: 98px; height: 20px; border-radius: 4px; background: var(--button); color: var(--button-text); font-size: 10.5px; display: flex; align-items: center; justify-content: center; }
  .band { position: absolute; left: 0; top: 521px; width: 100%; height: 28px; background: var(--lilac); }

  .welcome { position: absolute; left: 0; top: 549px; width: 100%; height: 262px; background: var(--blush); }
  .welcome-title { position: absolute; left: 63px; top: 52px; font-family: var(--serif); font-weight: 600; font-size: 36px; line-height: 38.5px; color: var(--berry); }
  .welcome-text { position: absolute; right: 67px; top: 75px; width: 400px; text-align: right; font-size: 13.3px; line-height: 15.4px; color: var(--berry); }
  .scallop--home { position: absolute; left: 0; top: 811px; width: 828px; height: 37px; }
</style>
</head>
<body>

  <section class="page page--scroll" aria-label="Home page, scrolled view">
    <header class="site-header">
      <div class="brand"><span class="brand-dot"></span><span class="brand-name">Orla Maskrade<br>Beauty Lounge</span></div>
      <ul class="main-nav"><li>Home</li><li>Glam Anywhere</li><li>Glam Store</li><li>Trinidad</li><li>More</li></ul>
    </header>
    <div class="hero" role="img" aria-label="Carnival masquerader in a jewelled gold headpiece and beaded costume"></div>
    <h2 class="hero-title">Get Glam for<br>Carnival 2026</h2>
    <div class="band"></div>
    <div class="scroll-intro">
      <p>We specialize in bold, beautiful, and unforgettable carnival looks designed to make you feel like the main character. Whether you're prepping for Trinidad and Tobago Carnival or a special event, our expert makeup artists are here to bring your vision to life. From glitter and lashes to full-face glam, we've got you covered. Get ready to shine, sparkle, and slay the stage with confidence!</p>
    </div>
    <svg class="scallop--scroll" viewBox="0 0 486 21" preserveAspectRatio="none" aria-hidden="true">
      <path d="M0 0 H486 V0 A60.75 21 0 0 1 364.5 0 A60.75 21 0 0 1 243 0 A60.75 21 0 0 1 121.5 0 A60.75 21 0 0 1 0 0 Z" fill="#ffcac4"/>
    </svg>
    <h3 class="why-title">Why choose us? It’s a luxury lounge, not a panic room.</h3>
    <p class="why-text">See the works we have done with different colors, costumes and more!</p>
    <div class="gallery-photo gallery-photo--one" role="img" aria-label="Carnival costume makeup look"></div>
    <div class="gallery-photo gallery-photo--two" role="img" aria-label="Dancer in black fringe costume with red feather headdress"></div>
    <div class="gallery-photo gallery-photo--three" role="img" aria-label="Performer with white feather fans on stage"></div>
    <svg class="gallery-arrow" viewBox="0 0 14 28" aria-hidden="true"><path d="M2 2 L12 14 L2 26" fill="none" stroke="#d6a6dd" stroke-width="2.5" stroke-linecap="round" stroke-linejoin="round"/></svg>
    <div class="services">
      <div class="services-photo" role="img" aria-label="Two carnival dancers in sequinned blue costumes"></div>
      <h3 class="services-title">Services</h3>
      <p class="services-sub">Choose the service you need and allow us to be a part of your beautiful journey!</p>
      <ul class="service-list">
        <li class="service-item"><small>+ See more</small>Make up</li>
        <li class="service-item"><small>+ See more</small>Hair Style</li>
        <li class="service-item"><small>+ See more</small>Lashes</li>
        <li class="service-item"><small>+ See more</small>Body Care</li>
        <li class="service-item"><small>+ See more</small>Glitter</li>
      </ul>
    </div>
  </section>

  <section class="page page--home" aria-label="Home page, top view">
    <header class="site-header">
      <div class="brand"><span class="brand-dot"></span><span class="brand-name">Orla Maskrade<br>Beauty Lounge</span></div>
      <ul class="main-nav"><li>Home</li><li>Glam Anywhere</li><li>Glam Store</li><li>Trinidad</li><li>More</li></ul>
    </header>
    <div class="hero" role="img" aria-label="Carnival masquerader waving, wearing a jewelled gold headpiece and green beaded costume"></div>
    <h1 class="hero-title">Get Glam for<br>Carnival 2026</h1>
    <a class="book-button">Book Now</a>
    <div class="band"></div>
    <div class="welcome">
      <h2 class="welcome-title">Welcome to<br>Orla Maskrade<br>Beauty Lounge</h2>
      <p class="welcome-text">We specialize in bold, beautiful, and unforgettable carnival looks designed to make you feel like the main character. Whether you're prepping for Trinidad and Tobago Carnival or a special event, our expert makeup artists are here to bring your vision to life. From glitter and lashes to full-face glam, we've got you covered. Get ready to shine, sparkle, and slay the stage with confidence!</p>
    </div>
    <svg class="scallop--home" viewBox="0 0 828 37" preserveAspectRatio="none" aria-hidden="true">
      <path d="M0 0 H828 V0 A69 37 0 0 1 690 0 A69 37 0 0 1 552 0 A69 37 0 0 1 414 0 A69 37 0 0 1 276 0 A69 37 0 0 1 138 0 A69 37 0 0 1 0 0 Z" fill="#ffcac4"/>
    </svg>
  </section>

</body>
</html>
```